Nu Shield Total Project

We are a wireless internet service provider (WISP). We are launching a new service to our customers called "Nu Shield Total". This new program will provide the following services to our customers as part of the $8.95 monthly service fee:
In-Home service calls are free
Provide WiFi Router
Router Support and Configuration
Free Cable Move (1 per year)
Cable Repair
Anti-Virus protection software
We will also be offering these services for additional charges:
Internet Security Suite $4.95 /month
Online Backup Storage - $4.99 /month
Target Market(s)
Current customers that use our internet service.
Industry/Entity Type
Wireless Internet
Look and feel
Each slider illustrates characteristics of the customer's brand and the style your logo design should communicate.

```html
<!DOCTYPE html>
<html lang="en">
<head>
<meta charset="utf-8">
<title>Nu Shield Total</title>
<link href="https://fonts.googleapis.com/css2?family=Poppins:wght@500;600&display=swap" rel="stylesheet">
<style>
  :root {
    --page-bg: #eeeeee;
    --flyer-bg: #fcfbf7;
    --flyer-edge: #c9c9c9;
    --brand-red: #f20d0d;
    --brand-blue: #2b3fd9;
    --logo-blue: #1d2f9e;
    --white: #ffffff;
  }
  * { margin: 0; padding: 0; box-sizing: border-box; }
  html, body {
    width: 858px; height: 1200px; overflow: hidden;
    background: var(--page-bg);
    font-family: "Poppins", sans-serif;
  }
  .flyer {
    position: absolute; left: 6px; top: 52px;
    width: 845px; height: 1096px;
    background: var(--flyer-bg);
    border: 1px solid var(--flyer-edge);
    overflow: hidden;
  }
  .hero-photo {
    position: absolute; left: 52px; top: 43px;
    width: 657px; height: 471px;
    border-radius: 40px;
    background: linear-gradient(135deg, #e9eef0 0%, #d8dee0 45%, #c9b59a 70%, #eef2f3 100%);
  }
  .hero-curve { position: absolute; left: 0; top: 0; width: 845px; height: 260px; }
  .brand {
    position: absolute; left: 612px; top: 62px;
    display: flex; align-items: center; gap: 10px;
    color: var(--logo-blue); font-weight: 600;
    font-size: 17px; line-height: 1.1; letter-spacing: 0.5px;
  }
  .brand-mark { width: 24px; height: 24px; background: var(--logo-blue); flex: none; }
  .headline {
    position: absolute; color: var(--brand-red);
    font-weight: 500; font-size: 84px; line-height: 1; letter-spacing: -1px;
    white-space: nowrap;
  }
  .headline--first { left: 72px; top: 436px; }
  .headline--second { left: 198px; top: 521px; }
  .price-line {
    position: absolute; left: 80px; top: 594px;
    color: var(--brand-blue); font-weight: 600; font-size: 38px; white-space: nowrap;
  }
  .price-line .amount { font-size: 56px; }
  .benefits {
    position: absolute; left: 80px; top: 713px;
    list-style: none; color: var(--brand-blue);
    font-weight: 600; font-size: 26px; line-height: 44px;
    white-space: nowrap;
  }
  .benefits li::before { content: "\2022"; margin-right: 12px; }
  .addon {
    position: absolute; left: 580px; width: 265px; height: 95px;
    background: var(--brand-red); color: var(--white);
    text-align: right; padding: 22px 24px 0 0; font-weight: 500;
  }
  .addon-name { font-size: 17px; line-height: 1.35; }
  .addon-price { font-size: 22px; line-height: 1.3; font-weight: 600; }
  .addon--backup { top: 846px; }
  .addon--security { top: 961px; }
</style>
</head>
<body>
  <main class="flyer">
    <div class="hero-photo" role="img" aria-label="Photo of a smiling couple using a laptop together at home"></div>
    <svg class="hero-curve" viewBox="0 0 845 260" aria-hidden="true">
      <path d="M490 0 C515 120 610 175 712 200 L712 0 Z" fill="var(--flyer-bg)"/>
    </svg>
    <div class="brand">
      <span class="brand-mark"></span>
      <span>MESA BREEZE<br>WIRELESS</span>
    </div>

    <h1 class="headline headline--first">Nu Shield</h1>
    <h1 class="headline headline--second">Total</h1>

    <p class="price-line"><span class="amount">$8.95</span> monthly service fee:</p>

    <ul class="benefits">
      <li>n-Home service calls are free</li>
      <li>Provide WiFi Router</li>
      <li>Router Support and Configuration</li>
      <li>Free Cable Move (1 per year)</li>
      <li>Cable Repair</li>
      <li>Anti-Virus protection software</li>
    </ul>

    <div class="addon addon--backup">
      <div class="addon-name">Online Backup Storage</div>
      <div class="addon-price">$4.99 /month</div>
    </div>
    <div class="addon addon--security">
      <div class="addon-name">Internet Security Suite</div>
      <div class="addon-price">$4.95 /month</div>
    </div>
  </main>
</body>
</html>
```